Label for Whiskey and Rum Bottle

We are a distillery. Whiskey and Rum We like to have a new label for our bottles. The whiskey bottles are in a wooden case. http://www.korntropfen-muster.ch/store/product/tannwalder-oberkamm-single-malt-whiskey-nr-6 The Rum Bottles have no package. The label is even more important. http://www.korntropfen-muster.ch/store/product/tannwalder-oberkämmer-rum You can see the form of the bottles here www.korntropfen-muster.ch/store Whiskey and rum bottles are for a liter (50 cl) The labels can be with a picture or without. We would like to have something completely new. Therefore we don`t like to make much prescriptions concerning the design. We don`t like to give too much information (text) on the label. Just the information required by law. Consumers should understand the labels without long-reading. (The label-text is below) The 2 labels (Whiskey and rum) should look similar. Probably they have a different color or a different picture or .... It should be clear that the 2 products are from the same distillery. We have the intention to change all our existing labels over time. This gives designers the chance for follow-up projects.

Target Market(s)

Adults, liquor lovers

Requirements
Must have
• Information on the label is in German. (See "") Whiskey: - the name of the whiskey is "Tannwald Ridgeside Single Malt Whiskey" - The Whiskey was matured 5 years in a sherry "5 years in the sherry barrel stored" - The Alcohol content is 40% volumes "40% Vol "- The bottle contents 50 cl" 5 dl "- The distillery is" Distillery Brugghofer, Felsmatt, www.korntropfen-muster.ch "- The producer is" Korvix GmbH "Rum: - The name is" Tannwald Ridgesider Rum "- The alcohol content is 37% Volumes "37% Vol" - The bottle contens 50 cl "5 dl" - The distillery is "Distillery Brugghofer, Felsmatt, www.korntropfen-muster.ch" - The producer is "Korvix GmbH"
Nice to have
• Premium looking label Only front label preferred Only necessary text on the label
Should not have
• No special print techniques necessary No special paper form

```html
<!DOCTYPE html>
<html lang="de">
<head>
<meta charset="utf-8">
<title>Tannwalder Oberkamm Single Malt Whiskey – Etikett</title>
<link rel="stylesheet" href="https://fonts.googleapis.com/css2?family=Coustard:wght@900&family=Oswald:wght@500&family=Archivo+Black&family=Pinyon+Script&family=Mrs+Saint+Delafield&display=swap">
<style>
  :root {
    --backdrop: #000000;
    --paper: #c5c0bb;
    --ink: #1c1b1a;
    --figure-light: #a8a197;
    --figure-dark: #7d766c;
    --copper-light: #f2b36a;
    --copper-mid: #c77a35;
    --copper-dark: #7a4419;
  }
  * { margin: 0; padding: 0; box-sizing: border-box; }
  html, body {
    width: 1200px; height: 1200px; overflow: hidden;
    background: var(--backdrop);
  }
  .canvas { position: relative; width: 1200px; height: 1200px; }
  .label {
    position: absolute; left: 258px; top: 138px;
    width: 686px; height: 918px;
  }
  .label-paper { position: absolute; inset: 0; width: 100%; height: 100%; }
  .label-illustration {
    position: absolute; left: 134px; top: 94px;
    width: 440px; height: 664px;
    background: radial-gradient(ellipse at 50% 40%, var(--figure-light) 0%, var(--figure-dark) 60%, rgba(125,118,108,0) 100%);
    opacity: .55;
    border-radius: 45% 45% 20% 20%;
  }
  .volume {
    position: absolute; left: 16px; top: 50px;
    font: 500 22px/1.25 "Oswald", sans-serif;
    letter-spacing: .5px; color: var(--ink);
  }
  .producer-signature {
    position: absolute; left: 150px; top: 56px; width: 500px;
    font: 36px/1 "Mrs Saint Delafield", cursive; color: var(--ink);
  }
  .producer-signature::after {
    content: ""; position: absolute; left: 190px; right: 4px; top: 30px;
    border-top: 1px solid var(--ink);
  }
  .arched-title { position: absolute; left: 0; top: 420px; width: 686px; height: 90px; }
  .arched-title text {
    font: 900 40px "Coustard", serif; fill: var(--ink); letter-spacing: 2px;
  }
  .spirit-type {
    position: absolute; left: 0; right: 0; top: 494px; text-align: center;
    font: 44px/1 "Archivo Black", sans-serif;
    background: linear-gradient(180deg, var(--copper-light) 0%, var(--copper-mid) 55%, var(--copper-dark) 100%);
    -webkit-background-clip: text; background-clip: text; color: transparent;
  }
  .product-name {
    position: absolute; left: 0; right: 0; top: 554px; text-align: center;
    font: 900 56px/1.2 "Coustard", serif; color: var(--ink); letter-spacing: 1px;
  }
  .distillery {
    position: absolute; left: 0; right: 0; top: 692px; text-align: center;
    font: 500 28px/1 "Oswald", sans-serif; color: var(--ink); letter-spacing: .5px;
  }
  .maturation {
    position: absolute; left: 0; right: 0; top: 738px; text-align: center;
    font: 24px/1 "Pinyon Script", cursive; color: var(--copper-mid);
  }
  .origin {
    position: absolute; left: 0; right: 0; top: 800px; text-align: center;
    font: 500 28px/1 "Oswald", sans-serif; color: var(--ink); letter-spacing: .5px;
  }
</style>
</head>
<body>
<main class="canvas">
  <article class="label">
    <svg class="label-paper" viewBox="0 0 686 918" preserveAspectRatio="none" aria-hidden="true">
      <path fill="#c5c0bb" d="M0 6 L20 3 L38 7 L60 2 L84 6 L104 3 L130 8 L152 4 L176 7 L200 2 L226 6 L250 3 L274 8 L300 4 L322 7 L348 2 L372 6 L396 3 L420 8 L444 4 L468 7 L494 2 L518 6 L542 3 L566 8 L590 4 L614 7 L640 3 L664 6 L686 4 L686 918 L0 918 Z"/>
    </svg>

    <div class="label-illustration" role="img" aria-label="Stich eines Küfers, der zwei Holzfässer auf den Schultern trägt"></div>

    <p class="volume">40% VOL<br>5 DL</p>
    <p class="producer-signature">Korvix GmbH</p>

    <svg class="arched-title" viewBox="0 0 686 90">
      <path id="single-malt-arc" d="M170 78 Q343 34 516 78" fill="none"/>
      <text text-anchor="middle"><textPath href="#single-malt-arc" startOffset="50%">SINGLE MALT</textPath></text>
    </svg>

    <p class="spirit-type">Whiskey</p>
    <h1 class="product-name">TANNWALDER<br>OBERKAMM</h1>
    <p class="distillery">BRENNEREI BRUGGHOFER</p>
    <p class="maturation">5 Jahre Im Sherry Fass Gelagert</p>
    <p class="origin">PRODUKT FRÅN SCHWEIZ</p>
  </article>
</main>
</body>
</html>
```